Page Layouts for Australian Political Party

The Forward Signal Party of Australia has a design for its logo and now is looking for a website proposal. The initial website is being powered by blogger with plans to move to an ExpressionEngine based site. The current website is at www.fspartyhub.org

Its likely if we see a design within the next 2 days we like it will be selected before the 5 days has expired.

Target Market(s)

Looking for a design that will appeal to both the "online" generation as well as more casual internet users. These users might be comfortable with online banking and perhaps mailnest/talkloop but not much more.

I personally like the "feel" of vimrol.com and plumtreelabs.com. You might like to look at the other major political parties in Australia to see what probably quite a lot of "market testing" and money is acceptable to the Australian population. We are aiming for Generation X and younger and well as the baby boomers who get the 2.0 internet.

Industry/Entity Type

Political

Requirements
Must have
• The ability to scale elegantly across a full ExpressionEngine implementation, forums, blogs, homepage etc.
• Also look elegant on the initial blogger driven page.
• Navigation that could contain all the items on the www.unityfront.org.au site, you can use these as the place holder names for the navigation design. The short name for the party is FSP. The
Nice to have
• feel distinct from the other major parties websites. we do have views more in line with the orchardists/reformists in this country.
Should not have
• basic stuff, not look like a pagenook page ;) imagery too similar from any of the other parties...

```html
<!DOCTYPE html>
<html lang="en">
<head>
<meta charset="utf-8">
<title>Forward Signal Party of Australia – Blog</title>
<link rel="stylesheet" href="https://fonts.googleapis.com/css2?family=Arimo:wght@400;700&family=Luckiest+Guy&display=swap">
<style>
:root{
  --band:#3d3d3d;
  --band-dark:#333333;
  --paper:#ffffff;
  --ink:#111111;
  --muted:#777777;
  --cyan:#1aa3d6;
  --link:#1a8fe0;
  --gold:#f5b400;
  --red:#d3151b;
  --orange:#f07a00;
  --yellow:#f4f400;
  --green:#39d21c;
  --tab:#ffffff;
  --cat:#a8a8a8;
}
*{box-sizing:border-box;margin:0;padding:0}
html,body{width:1200px;height:900px;overflow:hidden;background:var(--paper);font-family:"Arimo",Arial,sans-serif;color:var(--ink)}
.page{position:relative;width:1200px;height:900px;overflow:hidden}

/* header */
.masthead{position:absolute;left:0;top:0;width:1200px;height:100px;background:var(--band);border-bottom:2px solid var(--red)}
.brand{position:absolute;left:138px;top:10px;display:flex;flex-direction:column;align-items:center;gap:8px}
.brand-mark{width:60px;height:60px;background:#2a3f9a;border-radius:6px}
.brand-name{color:#fff;font-size:21px;font-weight:700;letter-spacing:-.5px}
.subscribe{position:absolute;left:612px;top:24px;display:flex;align-items:center;font-size:11px}
.subscribe .lead{color:var(--cyan)}
.subscribe .label{color:#fff;margin-left:4px}
.subscribe .field{margin-left:12px;width:224px;height:26px;border-radius:5px;background:#fff;border:1px solid #ccc;color:#c8c8c8;font-size:10px;padding:8px 0 0 10px}
.submit{position:absolute;left:995px;top:50px;color:#fff;font-size:11px;font-weight:700}
.tabs{position:absolute;left:551px;top:84px;display:flex;gap:11px}
.tabs a{display:block;height:17px;background:var(--tab);border-radius:7px 7px 0 0;font-size:10.5px;text-align:center;line-height:18px;color:#222;text-decoration:none}
.tabs .watch{color:var(--red)}
.tabs .blog{color:var(--orange)}

/* post */
.post{position:absolute;left:134px;top:118px;width:880px;font-size:14.5px;line-height:16.5px}
.post-date{font-size:15px;letter-spacing:.3px;margin-bottom:18px}
.post-title{color:var(--gold);font-size:15px}
.post-intro{color:var(--muted);font-size:15px;margin-bottom:17px}
.post-intro a{color:var(--link);text-decoration:none}
.post p{margin-bottom:16px}
.post b{font-weight:700}
.scrollbar{position:absolute;left:1047px;top:122px;width:21px;height:457px;border:1px solid #000;background:#fff}
.scrollbar .up,.scrollbar .down{position:absolute;left:4px;width:0;height:0;border-left:6px solid transparent;border-right:6px solid transparent}
.scrollbar .up{top:5px;border-bottom:9px solid #000}
.scrollbar .down{bottom:5px;border-top:9px solid #000}
.scrollbar .thumb{position:absolute;left:2px;top:50px;width:15px;height:28px;border-radius:7px;background:#111}

/* footer band */
.footband{position:absolute;left:0;top:600px;width:1200px;height:90px;background:var(--band);border-top:2px solid var(--red)}
.tagline{position:absolute;left:133px;top:10px;color:#fff;font-size:11.5px}
.tagline-echo{position:absolute;left:133px;top:26px;color:#fff;font-size:11.5px;opacity:.25;transform:scaleY(-1)}
.social{position:absolute;left:708px;top:590px;display:flex;gap:16px}
.social span{display:block;width:29px;height:29px;border-radius:3px}
.categories{position:absolute;left:130px;top:650px;width:940px;height:40px;background:#fff;border-radius:6px 6px 0 0;padding:16px 0 0 10px;font-size:11px;font-weight:700;color:var(--cat);white-space:nowrap}
.categories i{font-style:normal;color:var(--red);margin:0 6px}

/* promo tiles */
.promo{position:absolute;top:706px;width:302px;height:121px;background:var(--band-dark);border:3px solid;border-radius:4px;overflow:hidden}
.promo .art{position:absolute}
.promo .head{position:absolute;font-family:"Luckiest Guy",Impact,sans-serif;color:#fff;line-height:1}
.promo-say{left:130px;border-color:var(--red)}
.promo-join{left:448px;border-color:var(--yellow)}
.promo-plan{left:765px;border-color:var(--green)}
.echo{position:absolute;top:830px;width:302px;height:42px;border:3px solid;border-radius:4px;opacity:.22;background:linear-gradient(#555,#fff)}
</style>
</head>
<body>
<div class="page">

  <header class="masthead">
    <div class="brand"><span class="brand-mark"></span><span class="brand-name">Forward Signal</span></div>
    <div class="subscribe"><span class="lead">FOR UP-TO-DATE NEWS</span><span class="label">SUBSCRIBE:</span><span class="field">INSERT EMAIL ADDRESS</span></div>
    <div class="submit">SUBMIT</div>
    <nav class="tabs">
      <a style="width:73px">HOME</a>
      <a style="width:73px">PROFILE</a>
      <a style="width:73px">TEAM</a>
      <a style="width:73px">NEWS</a>
      <a class="watch" style="width:73px">WATCH</a>
      <a class="blog" style="width:73px">BLOG</a>
    </nav>
  </header>

  <article class="post">
    <div class="post-date">MONDAY, MARCH 29, 2010</div>
    <div class="post-title">ISP Censorship WILL NOT Make Kids Safe Online.</div>
    <div class="post-intro">This is taken from the transcript of an interview with <a>Ray Hollis on Straight Talk...</a></div>
    <p>Martin Cole: So they (the Unity Front government) knew what was good for people better than people themselves?</p>
    <p><b>Ray Hollis</b>: They reckoned they did yeah. I think censorship is evil Martin, because it's the beginning of the beginning of the big brother state, and if you start censoring matter from facts from people then it's an easy step to censor all sorts of things, and then they don't know what's going on. We've got the Tampa incident, the children overboard incident, there was censorship. They were lies in my view.</p>
    <p><b>Martin Cole</b>: What you're talking about with Tampa is effectively freedom of information. How do we enshrine freedom of information so there can be no censorship of material people need to judge?</p>
    <p><b>Ray Hollis</b>: Only with the good will of politicians and I don't think either party would agree to that.</p>
    <p><b>Martin Cole</b>: Why not?</p>
    <p><b>Ray Hollis</b>: Well it's against their interest. They love having secrets.</p>
    <p><b>Martin Cole</b>: But aren't they representing our interests?</p>
    <p><b>Ray Hollis</b>: Yeah.</p>
    <p><b>Martin Cole</b>: Whose interests are they representing first, ours or theirs?</p>
  </article>
  <div class="scrollbar"><span class="up"></span><span class="thumb"></span><span class="down"></span></div>

  <section class="footband">
    <div class="tagline">EMPOWERING THE PEOPLE VIA THE INTERNET TO IMPLEMENT A FAIR AND JUST FUTURE FOR EVERYONE.</div>
    <div class="tagline-echo" aria-hidden="true">EMPOWERING THE PEOPLE VIA THE INTERNET TO IMPLEMENT A FAIR AND JUST FUTURE FOR EVERYONE.</div>
  </section>
  <div class="social" aria-label="Social links">
    <span style="background:#c4161c"></span>
    <span style="background:#2d5aa0"></span>
    <span style="background:#3fb3e0"></span>
    <span style="background:#e8741c"></span>
    <span style="background:#e6e6e6"></span>
    <span style="background:#8a8a8a"></span>
    <span style="background:#1c3d8c"></span>
    <span style="background:#ef7a1a"></span>
  </div>
  <nav class="categories">ECONOMY<i>|</i>SMALL BUSINESS<i>|</i>NATIONAL SECURITY<i>|</i>COMMUNITY<i>|</i>SENIORS<i>|</i>HEALTH<i>|</i>EDUCATION<i>|</i>ENVIRONMENT<i>|</i>REGIONAL<i>|</i>INFRASTRUCTURE</nav>

  <a class="promo promo-say">
    <div class="art" role="img" aria-label="Two red speech bubbles" style="left:105px;top:-8px;width:190px;height:56px;background:var(--red);border-radius:8px"></div>
    <div class="head" style="left:10px;top:40px;font-size:34px">HAVE YOUR SAY!</div>
    <div class="head" style="left:10px;top:82px;font-size:23px">Your Opinion Matters</div>
  </a>
  <a class="promo promo-join">
    <div class="art" role="img" aria-label="Yellow silhouette of a cheering crowd" style="left:0;top:62px;width:296px;height:56px;background:var(--yellow)"></div>
    <div class="head" style="left:12px;top:14px;font-size:54px">JOIN US!</div>
  </a>
  <a class="promo promo-plan">
    <div class="art" role="img" aria-label="Green map of Australia and surrounding region" style="left:130px;top:0;width:166px;height:96px;background:var(--green);opacity:.9;border-radius:0 0 0 40px"></div>
    <div class="head" style="left:7px;top:4px;font-size:38px">10 <span style="font-size:26px">WAYS TO</span></div>
    <div class="head" style="left:7px;top:48px;font-size:28px">HELP SAVE</div>
    <div class="head" style="left:7px;top:82px;font-size:28px">YOUR PLANT</div>
  </a>
  <div class="echo" aria-hidden="true" style="left:130px;border-color:var(--red)"></div>
  <div class="echo" aria-hidden="true" style="left:448px;border-color:var(--yellow)"></div>
  <div class="echo" aria-hidden="true" style="left:765px;border-color:var(--green)"></div>
</div>
</body>
</html>
```